Stylish, Masculine Design - Men's Clothing

Granary Coat Mart is a 14,000 square foot warehouse outlet store open to the public since 2005. 50+ brands. Well-known designer brand names and private labels. 30-80% off retail everyday. Lowest prices guaranteed. Average suit price $150. Average shirt price $20. One-stop shop shopping. Men's suits, tuxedos, tuxedo rentals, dress shirts, ties, dress shoes, boy's suits and tuxedos, clergy robes, clergy shirts, cologne, loungewear. Slim fits (Prom Dance), business styles, "church" fashion, security-related uniform. Alterations done by expert tailors on premises for an extra charge.
The final design for both business card and logo should portray stylishness and masculinity.
Updates
We will be changing our name. Details below.New name: Warehouse Suit & TuxFormer name: Granary Coat Mart Added Monday, December 26, 2016
Target Market(s)
Gender: 80% Male, 15% Female, 5% Transgender
Location: 80% 10 Mile Radius, 20% >10 Mile Radius
Age: 17-18 (Primarily prom), 18-35 (Primarily Interviews and Weddings), 36-70 (primarily Church and events)
Race: African-American 50%, Latino-American 20%, White 15%, 10% Asian 5% Other
Religions: Christian 50%, 20% Catholic, 10% Mormon, 20% Other/None
Occupation: Local government 40%, Large corporation employee 20%, Small business employee 10%, Small business owner 10%, 20% Unemployed (high school, college)
Education: High School or equivalent 40%, College 30%, Some College 20%, Masters/Doctors 10%
Industry/Entity Type
Retail
Contact Information for Business Card
Name: Peter Olund
Title: Sales Associate
Address: 418 E. Mirabeth Ave. Larkmoor, CA 90247
Phone Number: 310.555.0182
Slogan: Wide Selection. Outlet Prices, Outstanding Service
www.granarycoatmart.example
Logo Text
GCM (Acronym for Granary Coat Mart) or Image
Requirements
Must have
- Easy to read
- Visually appealing

```html
<!DOCTYPE html>
<html lang="en">
<head>
<meta charset="utf-8">
<title>Granary Coat Mart — Business Card</title>
<link rel="stylesheet" href="https://fonts.googleapis.com/css2?family=Open+Sans:wght@300;400;600&display=swap">
<style>
  :root {
    --backdrop: #3b3b3d;
    --card: #252527;
    --red: #e31e24;
    --white: #ffffff;
    --muted: #c9c9c9;
  }
  * { margin: 0; padding: 0; box-sizing: border-box; }
  html, body {
    width: 1200px; height: 1000px; overflow: hidden;
    background: var(--backdrop);
    font-family: "Open Sans", Arial, sans-serif;
  }
  .card {
    position: absolute; left: 100px; top: 214px;
    width: 1000px; height: 572px;
    background: var(--card);
    border-radius: 34px;
    overflow: hidden;
    box-shadow: 0 20px 50px rgba(0,0,0,.35);
  }
  .name-tab {
    position: absolute; left: 0; top: 150px;
    width: 26px; height: 112px;
    background: var(--red);
    border-radius: 0 22px 22px 0;
  }
  .person { position: absolute; left: 74px; top: 160px; }
  .person-name {
    font-size: 40px; font-weight: 600; letter-spacing: 1px;
    color: var(--white); line-height: 1.1;
  }
  .person-name .surname { color: var(--red); }
  .person-title {
    font-size: 25px; font-weight: 400; color: var(--white);
    margin-top: 4px;
  }
  .contact { position: absolute; left: 74px; top: 318px; color: var(--muted); }
  .address { font-size: 20px; font-weight: 300; line-height: 1.35; margin-left: 46px; }
  .contact-list { list-style: none; margin-top: 8px; }
  .contact-list li {
    display: flex; align-items: center;
    font-size: 20px; font-weight: 400; color: var(--white);
    height: 32px;
  }
  .contact-list svg { width: 18px; height: 18px; margin-right: 28px; flex: none; }
  .contact-list .accent { color: var(--red); }
  .brand {
    position: absolute; right: 70px; top: 210px;
    display: flex; align-items: center; gap: 18px;
  }
  .brand-square { width: 22px; height: 22px; background: var(--red); flex: none; }
  .brand-name {
    font-size: 36px; font-weight: 400; letter-spacing: 3px;
    color: var(--white); line-height: 1.15; text-transform: uppercase;
  }
  .slogan-band {
    position: absolute; left: 0; right: 0; bottom: 0; height: 74px;
    background: var(--red);
    display: flex; align-items: center; justify-content: flex-end;
    padding-right: 74px;
  }
  .slogan { font-size: 22px; font-weight: 400; color: var(--white); letter-spacing: .3px; white-space: nowrap; }
</style>
</head>
<body>
  <article class="card">
    <div class="name-tab"></div>

    <header class="person">
      <h1 class="person-name">PETER <span class="surname">OLUND</span></h1>
      <p class="person-title">Sales Associate</p>
    </header>

    <section class="contact">
      <p class="address">418 E. Mirabeth Ave.<br>Larkmoor, CA 90247</p>
      <ul class="contact-list">
        <li>
          <svg viewBox="0 0 24 24" aria-hidden="true"><path fill="#e31e24" d="M6.6 10.8c1.4 2.8 3.8 5.1 6.6 6.6l2.2-2.2c.3-.3.7-.4 1-.2 1.1.4 2.3.6 3.6.6.6 0 1 .4 1 1V20c0 .6-.4 1-1 1C10.6 21 3 13.4 3 4c0-.6.4-1 1-1h3.5c.6 0 1 .4 1 1 0 1.3.2 2.5.6 3.6.1.3 0 .7-.2 1z"/></svg>
          310 555 0182
        </li>
        <li>
          <svg viewBox="0 0 24 24" aria-hidden="true"><path fill="#e31e24" d="M2 5h20v14H2z"/><path fill="none" stroke="#252527" stroke-width="2" d="M2 5l10 8 10-8"/></svg>
          peter@granarycoatmart.example
        </li>
        <li>
          <svg viewBox="0 0 24 24" aria-hidden="true"><circle cx="12" cy="12" r="10" fill="#e31e24"/><path fill="none" stroke="#252527" stroke-width="1.5" d="M2 12h20M12 2c3 3 3 17 0 20M12 2c-3 3-3 17 0 20"/></svg>
          <span>www.<span class="accent">granarycoatmart</span>.example</span>
        </li>
      </ul>
    </section>

    <div class="brand">
      <span class="brand-square"></span>
      <p class="brand-name">Granary<br>Coat &amp; Vest</p>
    </div>

    <footer class="slogan-band">
      <p class="slogan">Wide Selection | Outlet Prices | Outstanding Service</p>
    </footer>
  </article>
</body>
</html>
```